Brookvine Estates Business Card

Business Card:

Somewhere on front of card, please include Broker License Number: 5839261

Website is BrookvineEstates.com

Address is:
7216 Orchardpine Ave E
Saginaw, MI 48517

I'll let you use creative freedom on the rest; we obviously need Name, Title, Email (@BrookvineEstates.com), Office Phone, Cell Phone.

Don't want any special die-cutting, just a standard size business card.

On the back, include a place for the date and time of an appointment to be written in pen.

Industry/Entity Type

Business

Requirements
Must have
• Our logo, attached to email.

```html
<!DOCTYPE html>
<html lang="en">
<head>
<meta charset="utf-8">
<title>Brookvine Estates Business Card</title>
<link href="https://fonts.googleapis.com/css2?family=Open+Sans:wght@400;600;700&family=Arimo:wght@400&display=swap" rel="stylesheet">
<style>
  :root {
    --brand-blue: #2c2d8c;
    --ink-grey: #6b6b70;
    --rule-grey: #8a8a8f;
    --paper: #ffffff;
    --backdrop: #2a2b2e;
  }
  * { margin: 0; padding: 0; box-sizing: border-box; }
  html, body { width: 1200px; height: 750px; overflow: hidden; }
  body {
    background: var(--backdrop);
    display: flex;
    align-items: center;
    justify-content: center;
    gap: 40px;
    font-family: "Open Sans", sans-serif;
  }
  .card {
    position: relative;
    width: 540px;
    height: 309px;
    background: var(--paper);
    overflow: hidden;
    box-shadow: 0 10px 30px rgba(0,0,0,.45);
  }
  .wordmark {
    position: absolute;
    display: flex;
    align-items: center;
    gap: 8px;
    color: var(--brand-blue);
    font-weight: 700;
    white-space: nowrap;
  }
  .wordmark-square {
    width: 14px; height: 14px;
    background: var(--brand-blue);
  }

  /* Back */
  .card-back .wordmark { top: 30px; right: 34px; font-size: 26px; }
  .appointment {
    position: absolute;
    left: 40px; right: 40px; top: 110px;
  }
  .field-row { display: flex; align-items: flex-end; gap: 28px; height: 34px; }
  .field { display: flex; align-items: flex-end; flex: 1; }
  .field-label { color: var(--brand-blue); font-size: 14px; font-weight: 600; margin-right: 8px; line-height: 1; }
  .field-line { flex: 1; border-bottom: 1px solid var(--rule-grey); height: 1px; }
  .field-time { position: relative; }
  .ampm {
    position: absolute; right: 0; top: -24px;
    color: var(--brand-blue); font-size: 10px; font-weight: 600;
  }
  .write-line { border-bottom: 1px solid var(--rule-grey); height: 34px; }

  /* Front */
  .title-band {
    position: absolute; left: 0; right: 0; top: 28px; height: 96px;
    background: var(--brand-blue);
    color: var(--paper);
    padding: 46px 0 0 40px;
  }
  .person-name { font-size: 20px; font-weight: 700; line-height: 1.1; }
  .person-title { font-size: 14px; font-weight: 400; }
  .card-front .wordmark { top: 136px; right: 30px; font-size: 30px; }
  .contact {
    position: absolute; left: 40px; top: 150px;
    font-family: "Arimo", sans-serif;
    color: var(--ink-grey); font-size: 12.5px; line-height: 1.3;
  }
  .contact p { margin: 0; }
  .contact .license { margin-top: 10px; margin-bottom: 6px; }
  .contact-item { display: flex; align-items: center; gap: 10px; }
  .contact-item svg { width: 12px; height: 12px; fill: var(--brand-blue); flex: none; }
</style>
</head>
<body>

  <section class="card card-back" aria-label="Card back, appointment reminder">
    <div class="wordmark"><span class="wordmark-square"></span>Brookvine Estates</div>
    <div class="appointment">
      <div class="field-row">
        <div class="field"><span class="field-label">Date :</span><span class="field-line"></span></div>
        <div class="field field-time"><span class="field-label">Time :</span><span class="field-line"></span><span class="ampm">AM/PM</span></div>
      </div>
      <div class="write-line"></div>
      <div class="write-line"></div>
      <div class="write-line"></div>
    </div>
  </section>

  <section class="card card-front" aria-label="Card front, contact details">
    <div class="title-band">
      <p class="person-name">Martin Keller</p>
      <p class="person-title">President</p>
    </div>
    <div class="wordmark"><span class="wordmark-square"></span>Brookvine Estates</div>
    <div class="contact">
      <p>7216 Orchardpine Ave E</p>
      <p>Saginaw, MI 48517</p>
      <p class="license">Broker Lic No: 5839261</p>
      <p class="contact-item">
        <svg viewBox="0 0 24 24"><path d="M6.6 10.8a15 15 0 0 0 6.6 6.6l2.2-2.2c.3-.3.7-.4 1-.2 1.1.4 2.3.6 3.6.6.6 0 1 .4 1 1V20c0 .6-.4 1-1 1A17 17 0 0 1 3 4c0-.6.4-1 1-1h3.5c.6 0 1 .4 1 1 0 1.3.2 2.5.6 3.6.1.3 0 .7-.2 1z"/></svg>
        989 555 0142</p>
      <p class="contact-item">
        <svg viewBox="0 0 24 24"><path d="M7 1h10a2 2 0 0 1 2 2v18a2 2 0 0 1-2 2H7a2 2 0 0 1-2-2V3a2 2 0 0 1 2-2zm0 3v14h10V4zm5 15.5a1 1 0 1 0 0 2 1 1 0 0 0 0-2z"/></svg>
        989 555 0187</p>
      <p class="contact-item">
        <svg viewBox="0 0 24 24"><path d="M2 5h20v14H2zm2 2v.5l8 5 8-5V7zm0 2.9V17h16V9.9l-8 5z"/></svg>
        name@BrookvineEstates.com</p>
      <p class="contact-item">
        <svg viewBox="0 0 24 24"><circle cx="12" cy="12" r="10"/></svg>
        www.BrookvineEstates.com</p>
    </div>
  </section>

</body>
</html>
```